Tallowreed Advisory Partners Business Card Design

We have the logo we just need someone to design a modern business card design.

Name: Desmond Munkalt
Phone: 3055550148
Mobile: 9175550193
Web:www.tallowreedadvisory.example
email: dmunkalt@tallowreedadvisory.example
Company: Tallowreed Advisory Partners
Title: CEO

Address: 718 Quillmore Ave, Miami, Florida 33190

Target Market(s)

companies over 100 employees

Industry/Entity Type

Business

```html
<!DOCTYPE html>
<html lang="en">
<head>
<meta charset="utf-8">
<title>Tallowreed Advisory Partners – Business Card</title>
<link rel="stylesheet" href="https://fonts.googleapis.com/css2?family=Arimo:wght@400;700&display=swap">
<style>
  :root {
    --card-charcoal: #555555;
    --panel-grey: #dcdcdc;
    --brand-blue: #3a5cf8;
    --ink-grey: #555555;
    --paper-white: #ffffff;
  }
  * { margin: 0; padding: 0; box-sizing: border-box; }
  html, body {
    width: 1200px;
    height: 1000px;
    overflow: hidden;
    background: var(--paper-white);
    font-family: "Arimo", Arial, sans-serif;
  }
  .canvas { position: relative; width: 1200px; height: 1000px; }

  .card {
    position: absolute;
    top: 96px;
    width: 471px;
    height: 802px;
    background: var(--card-charcoal);
    border-radius: 48px;
  }
  .card--front { left: 116px; }
  .card--back  { left: 624px; }

  .panel {
    position: absolute;
    background: var(--panel-grey);
    border-radius: 26px;
  }
  .card--front .panel { left: 31px; top: 265px; width: 409px; height: 504px; }
  .card--back  .panel { left: 30px; top: 44px;  width: 410px; height: 484px; }

  .brand-disc {
    position: absolute;
    border-radius: 50%;
    background: var(--brand-blue);
    display: flex;
    align-items: center;
    justify-content: center;
  }
  .card--front .brand-disc { left: 109px; top: 44px; width: 252px; height: 252px; }
  .card--back  .brand-disc { left: 155px; top: 510px; width: 158px; height: 158px; }

  .brand-name {
    font-family: "Arimo", Arial, sans-serif;
    font-weight: 700;
    color: var(--paper-white);
    white-space: nowrap;
  }
  .brand-disc .brand-name { font-size: 27px; letter-spacing: 1px; }
  .brand-wordmark {
    position: absolute;
    left: 0; right: 0;
    top: 694px;
    text-align: center;
    font-size: 54px;
    line-height: 1;
    letter-spacing: 2px;
  }

  .centered-text {
    position: absolute;
    left: 0; right: 0;
    text-align: center;
    color: var(--ink-grey);
  }
  .person-name {
    top: 124px;
    font-size: 34px;
    line-height: 38px;
    color: var(--brand-blue);
  }
  .person-title { top: 162px; font-size: 28px; line-height: 36px; }
  .contact-lines { top: 374px; font-size: 27px; line-height: 36px; }
  .address-lines { top: 292px; font-size: 27px; line-height: 35.5px; }

  .writing-lines { position: absolute; left: 35px; top: 51px; }
</style>
</head>
<body>
<main class="canvas">

  <section class="card card--front" aria-label="Card front">
    <div class="panel">
      <p class="centered-text person-name">YOUR NAME HERE</p>
      <p class="centered-text person-title">Assistant</p>
      <p class="centered-text contact-lines">
        Ph: (000) 000-0000<br>
        Cel: (000) 000-0000<br>
        yourname@tallowreed.example
      </p>
    </div>
    <div class="brand-disc">
      <span class="brand-name">TALLOWREED</span>
    </div>
  </section>

  <section class="card card--back" aria-label="Card back">
    <div class="panel">
      <svg class="writing-lines" width="345" height="210" viewBox="0 0 345 210" aria-hidden="true">
        <g stroke="var(--ink-grey)" stroke-width="3">
          <line x1="0" y1="2" x2="345" y2="2"/>
          <line x1="0" y1="52" x2="345" y2="52"/>
          <line x1="0" y1="102" x2="345" y2="102"/>
          <line x1="0" y1="152" x2="345" y2="152"/>
          <line x1="0" y1="202" x2="345" y2="202"/>
        </g>
      </svg>
      <p class="centered-text address-lines">
        Line Address 1<br>
        Line Address 2<br>
        City | State 00000<br>
        www.tallowreed.example
      </p>
    </div>
    <div class="brand-disc" aria-hidden="true"></div>
    <p class="brand-name brand-wordmark">TALLOWREED</p>
  </section>

</main>
</body>
</html>
```